Tr construction holdings pty ltd

2 sided card black and red with white
Very professional and elegant

Target Market(s)

Construction and Development

Industry/Entity Type

Construction and development

Contact Information for Business Card

One side black, one side red/or white business logo in top corner, email: morgan@trbuildworks.example

Requirements
Should not have
• Blue

```html
<!DOCTYPE html>
<html lang="en">
<head>
<meta charset="utf-8">
<title>TR Construction Holdings – Business Card</title>
<link href="https://fonts.googleapis.com/css2?family=Roboto:wght@400;500;700&display=swap" rel="stylesheet">
<style>
  :root {
    --backdrop: #262626;
    --paper: #f1f1f1;
    --ink: #1d1d1f;
    --charcoal: #1f2023;
    --red: #d9412b;
    --white: #ffffff;
  }
  * { box-sizing: border-box; margin: 0; padding: 0; }
  html, body {
    width: 1200px; height: 1200px; overflow: hidden;
    background: var(--backdrop);
    font-family: 'Roboto', Arial, sans-serif;
  }
  .canvas { position: relative; width: 1200px; height: 1200px; }

  .card {
    position: absolute;
    width: 594px; height: 348px;
    background: var(--paper);
    border-radius: 22px;
    overflow: hidden;
  }
  .card--front { left: 298px; top: 200px; }
  .card--back  { left: 292px; top: 637px; }

  /* company name, set as plain text */
  .company-name {
    position: absolute;
    text-align: center;
    font-weight: 700;
    text-transform: uppercase;
  }
  .card--front .company-name {
    left: 0; right: 0; top: 108px;
    font-size: 38px; line-height: 46px;
    color: var(--ink);
  }
  .card--back .company-name {
    left: 305px; width: 275px; top: 130px;
    font-size: 24px; line-height: 30px;
    color: var(--white);
  }

  .front__web {
    position: absolute; left: 0; right: 0; top: 308px;
    display: flex; align-items: center; justify-content: center; gap: 18px;
    font-size: 15px; color: var(--ink);
  }
  .front__rule { width: 66px; height: 2px; background: var(--red); }
  .front__band {
    position: absolute; left: 0; right: 0; bottom: 0; height: 6px;
    background: var(--red);
  }

  /* back */
  .back__panel { position: absolute; inset: 0; }

  .contact { position: absolute; left: 40px; top: 78px; color: var(--ink); }
  .contact__name { font-size: 21px; font-weight: 700; color: var(--red); }
  .contact__role { font-size: 14.5px; margin-top: 5px; }
  .contact__list { list-style: none; margin-top: 26px; }
  .contact__list li {
    display: flex; align-items: center; gap: 14px;
    font-size: 14.5px; height: 22px;
  }
  .contact__icon { width: 15px; height: 15px; flex: none; }
  .contact__address { font-size: 14.5px; line-height: 21px; margin-top: 10px; }
</style>
</head>
<body>
<main class="canvas">

  <section class="card card--front">
    <div class="company-name">TR Construction<br>Holdings Pty Ltd</div>
    <div class="front__web">
      <span class="front__rule"></span>
      <span>www.trbuildworks.example</span>
      <span class="front__rule"></span>
    </div>
    <div class="front__band"></div>
  </section>

  <section class="card card--back">
    <svg class="back__panel" width="594" height="348" viewBox="0 0 594 348">
      <path d="M338,0 Q250,174 335,348 L594,348 L594,0 Z" fill="var(--charcoal)"/>
      <path d="M338,0 Q250,174 335,348" fill="none" stroke="var(--red)" stroke-width="4"/>
      <path d="M338,0 L348,0 Q264,174 345,348 L335,348 Q250,174 338,0 Z" fill="var(--charcoal)"/>
    </svg>

    <div class="contact">
      <div class="contact__name">Morgan Hale</div>
      <div class="contact__role">Managing Director</div>
      <ul class="contact__list">
        <li>
          <svg class="contact__icon" viewBox="0 0 16 16"><path d="M2 6 Q8 1 14 6 L12 8 L10 6.5 L6 6.5 L4 8 Z M4 9 L12 9 L13 14 L3 14 Z" fill="var(--red)"/></svg>
          <span>555-010-2040</span>
        </li>
        <li>
          <svg class="contact__icon" viewBox="0 0 16 16"><rect x="1" y="3" width="14" height="10" fill="var(--red)"/><path d="M1 3 L8 9 L15 3 M1 13 L6 7.5 M15 13 L10 7.5" stroke="var(--paper)" stroke-width="1.2" fill="none"/></svg>
          <span>morgan@trbuildworks.example</span>
        </li>
        <li>
          <svg class="contact__icon" viewBox="0 0 16 16"><circle cx="8" cy="8" r="6.5" fill="var(--red)"/><path d="M1.5 8 H14.5 M8 1.5 V14.5 M3 4.5 H13 M3 11.5 H13" stroke="var(--paper)" stroke-width="0.9"/><ellipse cx="8" cy="8" rx="3" ry="6.5" fill="none" stroke="var(--paper)" stroke-width="0.9"/></svg>
          <span>www.trbuildworks.example</span>
        </li>
      </ul>
      <p class="contact__address">18 Ridgeline Rd., Eastbrook,<br>Harlow, US 204518</p>
    </div>

    <div class="company-name">TR Construction<br>Holdings Pty Ltd</div>
  </section>

</main>
</body>
</html>
```